The Polish & Glow Studio Website Update

Hello. I am seeking to freshen up my website with a clean and easy feel that incorporates our modern chic style. Our services cater to mostly young professionals and modern moms.

We focus on natural nail care and gentle professional waxing. We are known for our cleanliness. Our clients like our current website, however I'm hoping to make it look even more professional and user friendly. Some clients have even said our current website feels welcoming, unlike other websites that in they feel give a snobbish vibe. I like clean lines, simple, fresh, and sometimes bold. Totally NOT a fan of whimsical.

I threw added an accent color to the color pallet...however it should be used in moderation. I am also open to other accent colors. I'd like the site to emphasize the Brazilian wax as much as nails, if not more than nail. The photos downloaded are just to give you a few images of who we are, however are not necessary. Current website www.thepolishandglowstudio.example

Target Market(s)

Females 30-55

Industry/Entity Type

Beauty Salon

Coding

Coded - Design and coding required

Number of Pages Required

5+ page

Font styles to use
Sans Serif

Colors
ffffff
1b1b1b
acd136
eeeeee
878787
c4c4c4
efefef
7f7f7f

Requirements
Must have
• Clean look
Nice to have
• Our logo
Should not have
• Whimsical

```html
<!DOCTYPE html>
<html lang="en">
<head>
<meta charset="utf-8">
<title>The Polish &amp; Glow Studio</title>
<link href="https://fonts.googleapis.com/css2?family=Raleway:wght@400;500;600;700&family=Lato:wght@400;700&display=swap" rel="stylesheet">
<style>
:root{
  --white:#ffffff;
  --ink:#1b1b1b;
  --accent:#acd136;
  --paper:#eeeeee;
  --paper-2:#efefef;
  --grey:#878787;
  --grey-2:#7f7f7f;
  --silver:#c4c4c4;
  --panel:#333333;
  --tile:#3a3a3a;
}
*{box-sizing:border-box;margin:0;padding:0}
html,body{width:1200px;height:2965px;overflow:hidden}
body{position:relative;background:var(--white);font-family:'Lato',sans-serif;color:var(--ink)}
.abs{position:absolute}
.center{transform:translate(-50%,-50%);white-space:nowrap;text-align:center}
.heading{font-family:'Raleway',sans-serif}

/* nav */
.site-nav{position:absolute;top:0;left:0;width:1200px;height:51px;background:#0f0f0f}
.site-nav a{position:absolute;top:0;height:51px;line-height:51px;color:var(--white);font-size:13px;text-decoration:none;font-family:'Lato',sans-serif}
.site-nav a.active{background:#3d3d3d;padding:0 18px;left:59px}

/* hero */
.hero{position:absolute;top:51px;left:0;width:1200px;height:582px;overflow:hidden}
.hero-photo{position:absolute;inset:0;background:linear-gradient(90deg,#b8893a 0%,#e3c27a 22%,#e9cfa8 42%,#2f63b3 62%,#1e4f9e 80%,#4a86cf 100%)}
.logo-box{position:absolute;left:364px;top:0;width:441px;height:155px;background:rgba(255,255,255,.93);display:flex;align-items:center;justify-content:center;gap:14px}
.logo-box .mark{width:18px;height:18px;background:#4a4a4a}
.logo-box .name{font-family:'Raleway',sans-serif;font-weight:500;font-size:34px;color:#4a4a4a}
.hero-diamond{position:absolute;width:152px;height:152px;transform:translate(-50%,-50%) rotate(45deg);background:repeating-linear-gradient(45deg,#2f2f2f 0 3px,#363636 3px 6px);border:2px solid var(--white);box-shadow:0 0 0 1px rgba(0,0,0,.2)}
.hero-diamond-label{position:absolute;transform:translate(-50%,-50%);color:var(--white);font-size:16px;text-align:center;line-height:1.25;font-family:'Lato',sans-serif}
.book-now{position:absolute;left:441px;top:491px;width:283px;height:67px;background:#0d0d0d;color:var(--white);font-family:'Raleway',sans-serif;font-size:28px;display:flex;align-items:center;justify-content:center;gap:12px}

/* welcome */
.welcome{position:absolute;top:633px;left:0;width:1200px;height:638px;background:var(--paper-2)}
.welcome h1{position:absolute;left:0;width:1200px;top:46px;text-align:center;font-family:'Raleway',sans-serif;font-weight:700;font-size:32px}
.welcome .intro{position:absolute;left:145px;width:910px;top:116px;text-align:center;font-size:12.5px;line-height:21px;color:#444}
.photo-diamond{position:absolute;width:140px;height:140px;transform:translate(-50%,-50%) rotate(45deg);border-radius:14px}
.node{position:absolute;width:14px;height:14px;background:var(--ink);transform:translate(-50%,-50%) rotate(45deg)}
.service-label{font-family:'Raleway',sans-serif;font-size:30px;font-weight:500}

/* service menu */
.service-menu{position:absolute;top:1271px;left:0;width:1200px;height:746px;background:repeating-linear-gradient(135deg,rgba(255,255,255,.03) 0 2px,transparent 2px 7px),linear-gradient(90deg,#2a2a2a 0%,#3e3e3e 45%,#8a8a8a 75%,#bdbdbd 100%);overflow:hidden}
.hand-photo{position:absolute;left:730px;top:0;width:470px;height:746px;background:radial-gradient(ellipse at 60% 55%,#e9c8b8 0%,#d9ab98 35%,rgba(160,140,135,.4) 70%,rgba(120,120,120,0) 100%)}
.service-menu h2{position:absolute;left:55px;top:52px;color:var(--white);font-family:'Raleway',sans-serif;font-weight:700;font-size:32px}
.service-menu .lead{position:absolute;left:55px;top:103px;width:680px;color:#d0d0d0;font-size:12px;line-height:22px}
.menu-tile{position:absolute;width:123px;height:123px;transform:translate(-50%,-50%) rotate(45deg);background:var(--tile);border:1px solid #8a8a8a;border-radius:10px}
.menu-tile.hub{background:#050505;border-color:#050505}
.tile-text{position:absolute;transform:translate(-50%,-50%);color:var(--white);font-size:16px;line-height:1.3;text-align:center;white-space:nowrap}
.tile-text.hub{font-family:'Raleway',sans-serif;font-size:22px}
.col-label{color:var(--white);font-family:'Raleway',sans-serif;font-size:22px}

/* contact */
.contact{position:absolute;top:2017px;left:0;width:1200px;height:500px;overflow:hidden}
.contact-photo{position:absolute;inset:0;background:linear-gradient(90deg,#d9b98c 0%,#f1e3cf 30%,#f6ede2 60%,#e2c39a 100%)}
.contact-card{position:absolute;left:142px;top:59px;width:941px;height:407px;background:rgba(255,255,255,.86);border:1px solid #aaa}
.contact-card .divider{position:absolute;left:457px;top:30px;width:1px;height:345px;background:#bbb}
.card-title{font-family:'Raleway',sans-serif;font-size:28px;font-weight:500}
.card-sub{font-family:'Raleway',sans-serif;font-size:21px;position:absolute}
.card-line{position:absolute;font-size:12px;color:#333}
.bar{position:absolute;background:var(--panel);color:var(--white);font-family:'Raleway',sans-serif;display:flex;align-items:center;justify-content:center}

/* testimonials */
.testimonials{position:absolute;top:2517px;left:0;width:1200px;height:379px;background:repeating-linear-gradient(135deg,rgba(255,255,255,.025) 0 2px,transparent 2px 7px),#2d2d2d}
.testimonials h2{position:absolute;left:0;width:1200px;top:110px;text-align:center;color:var(--white);font-family:'Raleway',sans-serif;font-weight:500;font-size:28px}
.testimonials .quote{position:absolute;left:120px;width:960px;top:214px;text-align:center;color:var(--white);font-weight:700;font-size:13px;line-height:28px}
.dot{position:absolute;width:10px;height:10px;border:2px solid var(--white);border-radius:50%;top:329px}
.dot.on{background:var(--white)}

/* footer */
.site-footer{position:absolute;top:2896px;left:0;width:1200px;height:69px;background:var(--white)}
.site-footer p{position:absolute;left:50px;top:27px;font-size:11px;color:#333}
.social{position:absolute;top:30px;width:12px;height:12px;border-radius:50%;background:#2b2b2b}
</style>
</head>
<body>

<nav class="site-nav">
  <a class="active" href="#">Home</a>
  <a href="#" style="left:180px">Schedule An Appointment</a>
  <a href="#" style="left:407px">Products and Services</a>
  <a href="#" style="left:609px">Careers</a>
  <a href="#" style="left:722px">Specials</a>
  <a href="#" style="left:836px">About Us</a>
  <a href="#" style="left:957px">FAQ</a>
  <a href="#" style="left:1050px">Contact Us</a>
</nav>

<header class="hero">
  <div class="hero-photo" role="img" aria-label="Close-up of a manicured hand with glossy blue and jeweled nails against gold décor"></div>
  <svg class="abs" style="left:0;top:0" width="1200" height="582">
    <polygon points="0,110 80,285 0,460" fill="rgba(255,255,255,.85)"/>
    <polygon points="1200,110 1120,285 1200,460" fill="rgba(255,255,255,.85)"/>
  </svg>
  <div class="logo-box"><span class="mark"></span><span class="name">The Polish &amp; Glow Studio</span></div>

  <div class="hero-diamond" style="left:137px;top:285px"></div>
  <svg class="abs" style="left:126px;top:230px" width="22" height="22" viewBox="0 0 22 22" fill="none" stroke="#fff" stroke-width="2"><rect x="2" y="8" width="18" height="12"/><line x1="11" y1="8" x2="11" y2="20"/><line x1="1" y1="8" x2="21" y2="8"/><path d="M11 8 C7 2 3 5 7 8 M11 8 C15 2 19 5 15 8"/></svg>
  <div class="hero-diamond-label" style="left:137px;top:295px">Purchase Gift<br>Cards Online</div>

  <div class="hero-diamond" style="left:1062px;top:295px"></div>
  <svg class="abs" style="left:1052px;top:241px" width="20" height="24" viewBox="0 0 20 24" fill="none" stroke="#fff" stroke-width="2"><rect x="2" y="1" width="16" height="22"/><line x1="6" y1="6" x2="8" y2="6"/><line x1="12" y1="6" x2="14" y2="6"/><line x1="6" y1="11" x2="8" y2="11"/><line x1="12" y1="11" x2="14" y2="11"/><line x1="6" y1="16" x2="8" y2="16"/><line x1="12" y1="16" x2="14" y2="16"/></svg>
  <div class="hero-diamond-label" style="left:1062px;top:298px">Schedule Online!</div>

  <a class="book-now">BOOK NOW <svg width="14" height="20" viewBox="0 0 14 20"><path d="M3 2 L11 10 L3 18" fill="none" stroke="#fff" stroke-width="3"/></svg></a>
</header>

<section class="welcome">
  <h1>WELCOME TO THE POLISH &amp; GLOW STUDIO</h1>
  <p class="intro">To be the #1 nail and wax salon in the Brookfield, CT area, offering the most meticulous manicures, pedicures, and waxing service. We use superior products, advanced techniques, and exceptional sanitation procedures to provide our clients with safe, quality services. Our knowledgeable and friendly staff is always happy to assist with any of your Polish &amp; Glow concerns.</p>

  <div class="abs" style="left:584px;top:197px;width:2px;height:380px;background:#555"></div>
  <div class="abs" style="left:440px;top:317px;width:145px;height:1px;background:#555"></div>
  <div class="abs" style="left:585px;top:453px;width:160px;height:1px;background:#555"></div>
  <div class="node" style="left:585px;top:318px"></div>
  <div class="node" style="left:585px;top:454px"></div>

  <div class="photo-diamond" style="left:332px;top:316px;background:linear-gradient(135deg,#f3d3c6 0%,#e8b6a4 40%,#c8202a 70%,#9a1a20 100%)" role="img" aria-label="Hand with glossy red manicured nails"></div>
  <div class="abs center service-label" style="left:332px;top:442px">NAILS</div>

  <div class="abs center service-label" style="left:840px;top:296px">WAX</div>
  <div class="photo-diamond" style="left:842px;top:454px;background:linear-gradient(135deg,#cfe3f2 0%,#8fc3e6 45%,#e4c3ae 75%,#c9a08a 100%)" role="img" aria-label="Esthetician in blue gloves performing a facial wax"></div>
</section>

<section class="service-menu">
  <div class="hand-photo" role="img" aria-label="Elegant hands with long red nails"></div>
  <h2>SERVICE MENU</h2>
  <p class="lead">Lorem ipsum dolor sit amet, consectetur adipiscing elit, sed do eiusmod tempor incididunt ut labore et dolore magna aliqua. Ut enim ad minim veniam, quis nostrud exercitation ullamco laboris nisi ut aliquip ex ea commodo consequat. Duis aute irure dolor in reprehenderit in voluptate velit esse cillum dolor</p>

  <div class="abs" style="left:361px;top:192px;width:1px;height:514px;background:#9a9a9a"></div>
  <div class="abs center col-label" style="left:247px;top:273px">NAIL</div>
  <div class="abs center col-label" style="left:470px;top:273px">WAX</div>
  <div class="abs" style="left:360px;top:283px;width:56px;height:56px;transform:translate(-50%,-50%) rotate(45deg);background:#2d2d2d;border:1px solid #ddd"></div>
  <svg class="abs" style="left:344px;top:272px" width="32" height="22" viewBox="0 0 32 22"><path d="M2 18 C8 18 12 12 14 6 C16 2 20 2 22 6 L30 16 C31 19 28 20 24 20 L4 20 Z" fill="#fff"/></svg>

  <div class="menu-tile" style="left:263px;top:380px"></div>
  <div class="tile-text" style="left:263px;top:380px">Signature<br>Manicure- $24</div>
  <div class="menu-tile" style="left:465px;top:380px"></div>
  <div class="tile-text" style="left:465px;top:380px">Brow<br>Design - $13</div>
  <div class="menu-tile" style="left:166px;top:489px"></div>
  <div class="tile-text" style="left:166px;top:489px">Gel Polish<br>Manicure - $34</div>
  <div class="menu-tile hub" style="left:362px;top:494px"></div>
  <div class="tile-text hub" style="left:362px;top:494px">Service<br>Menu</div>
  <div class="menu-tile" style="left:557px;top:489px"></div>
  <div class="tile-text" style="left:557px;top:489px">Chin - $10</div>
  <div class="menu-tile" style="left:263px;top:607px"></div>
  <div class="tile-text" style="left:263px;top:607px">Signature<br>Pedicure - $40</div>
  <div class="menu-tile" style="left:465px;top:607px"></div>
  <div class="tile-text" style="left:465px;top:607px">Brazilian $55</div>
</section>

<section class="contact">
  <div class="contact-photo" role="img" aria-label="Softly blurred salon interior in warm tones"></div>
  <div class="contact-card">
    <div class="divider"></div>
    <div class="abs center card-title" style="left:210px;top:53px">CONTACT US</div>
    <div class="card-sub" style="left:71px;top:96px">Our Address</div>
    <div class="card-line" style="left:95px;top:133px">The Polish &amp; Glow Studio</div>
    <div class="card-line" style="left:95px;top:163px">42 Elm Row</div>
    <div class="card-line" style="left:95px;top:190px">Brookfield, CT 06000</div>
    <div class="card-sub" style="left:71px;top:220px">Telephones</div>
    <div class="card-line" style="left:99px;top:258px"><b>Tel:</b> (555) 014-2938</div>
    <div class="card-sub" style="left:71px;top:293px">Email id</div>
    <div class="card-line" style="left:99px;top:331px">info@thepolishandglowstudio.example</div>

    <div class="abs center card-title" style="left:714px;top:54px">SERVICES BY</div>
    <div class="bar" style="left:540px;top:93px;width:320px;height:45px;font-size:22px">Appointment Only</div>
    <div class="card-line" style="left:574px;top:165px">Appointments Available:</div>
    <div class="bar" style="left:540px;top:192px;width:235px;height:39px;font-size:19px;font-weight:600">Daily</div>
    <div class="card-line" style="left:574px;top:250px">9am-8pm most days</div>
    <div class="card-line" style="left:574px;top:278px">Salon is only staffed for scheduled appointments.</div>
    <div class="bar" style="left:540px;top:314px;width:320px;height:44px;font-size:22px">Book Now</div>
  </div>
</section>

<section class="testimonials">
  <svg class="abs" style="left:549px;top:31px" width="76" height="76" viewBox="0 0 76 76">
    <circle cx="38" cy="38" r="35" fill="none" stroke="#fff" stroke-width="2"/>
    <path d="M24 26 H52 A4 4 0 0 1 56 30 V44 A4 4 0 0 1 52 48 H36 L28 55 V48 H24 A4 4 0 0 1 20 44 V30 A4 4 0 0 1 24 26 Z" fill="#fff"/>
    <circle cx="33" cy="37" r="3" fill="#2d2d2d"/><circle cx="43" cy="37" r="3" fill="#2d2d2d"/>
  </svg>
  <h2>CLIENT TESTIMONIALS</h2>
  <div class="abs" style="left:587px;top:152px;width:1px;height:59px;background:#aaa"></div>
  <p class="quote">Lorem ipsum dolor sit amet, consectetur adipiscing elit, sed do eiusmod tempor incididunt ut labore et dolore magna aliqua. Ut enim ad minim veniam,<br>quis nostrud exercitation ullamco laboris nisi ut aliquip ex ea commodo consequat.</p>
  <div class="abs" style="left:430px;top:292px;width:95px;height:1px;background:#bbb"></div>
  <div class="abs center" style="left:582px;top:292px;color:#fff;font-size:16px">Clara Wells</div>
  <div class="abs" style="left:652px;top:292px;width:95px;height:1px;background:#bbb"></div>
  <span class="dot" style="left:561px"></span>
  <span class="dot on" style="left:580px"></span>
  <span class="dot" style="left:599px"></span>
</section>

<footer class="site-footer">
  <p>All Rights Reserved. Copyrights @company Name. 2016</p>
  <span class="social" style="left:977px"></span>
  <span class="social" style="left:1016px"></span>
  <span class="social" style="left:1052px"></span>
  <span class="social" style="left:1088px"></span>
  <span class="social" style="left:1125px"></span>
</footer>

</body>
</html>
```